A4 Childcare Spring Special Flyer

Crestwell Learning is a registered training organisation (RTO) Toid No. 47318, based in Blackburn, Victoria. We are a market leader in Professional development courses both accredited and non accredited, in order for you to maintain currency in your profession.

We need a flyer for a childcare specific spring special. The special is to offer a $50 VOLM gift card and 50% of your second training session. Conditions apply*

The training sessions available are the NEW childcare specific course: HLTAID004 Provide an emergency first aid response in an education and care setting and HLTAID003 Provide First Aid, HLTAID001 Provide Cardiopulmonary Resuscitation (CPR), 22024VIC Course in emergency management of asthma in the workplace
and 22099VIC Course in First Aid Management of Anaphylaxis.
We provide a flexible, cost effective and reliable service.
We have training locations available in Blackburn, Preston, Narre Warren and Mornington and can also provide onsite training.

We can also provide education and PRIVOS regulation consultation to the childcare provider.

Must use company logo, include phone number: (03) 5127 6481, website: www.crestwelllearning.com.au, email: marapenn@crestwelllearning.com.au

(Note that a letter with more detail will be attached with this flyer, therefore, with that in mind; use that information as desired).

The final product should be as childcare like as possible whilst also keeping our company colors (same as logo). We would also like for this flyer to stand out and be appealing to the recipient as this flyer is to gain potential clients, with emphasis on the HLTAID004 Course
Updates

Just need to update the qualifications: In the design brief I mentioned that the course; HLTAID001 Provide CPR and Asthma & Anaphyalxis.. Can this please be changed to HLTAID001 Provide Cardiopulmonary Resuscitation (CPR) And 22024VIC Course in emergency management of asthma in the workplace And 22099VIC Course in First Aid Management of Anaphylaxis (They are all singular courses) Apoligies!

Target Market(s)

Childcare centres, Out of school hours providers, pre-schools

Industry/Entity Type

Childcare

Font styles to use
Decorative

Colors
ffcf3e
f37123
faa54b

Requirements
Must have
• Company Logo
phone number
website
email
Registered Training Organisation
TOID: 47318

```html
<!DOCTYPE html>
<html lang="en">
<head>
<meta charset="utf-8">
<title>Crestwell Learning – Childcare First Aid Training</title>
<link href="https://fonts.googleapis.com/css2?family=Crimson+Text:wght@400;600;700&display=swap" rel="stylesheet">
<style>
  :root {
    --yellow: #ffde00;
    --orange: #f15a22;
    --orange-soft: #f37123;
    --ink: #333333;
    --white: #ffffff;
    --photo-child: #9fa3a3;
    --photo-kitchen: #b08a6a;
    --photo-play: #e3735a;
  }
  * { margin: 0; padding: 0; box-sizing: border-box; }
  html, body { width: 849px; height: 1200px; overflow: hidden; background: var(--white); }
  .flyer {
    position: relative;
    width: 849px;
    height: 1200px;
    font-family: "Crimson Text", Georgia, serif;
    color: var(--ink);
  }
  .block { position: absolute; }
  .accent-yellow { left: 0; top: 40px; width: 263px; height: 242px; background: var(--yellow); }
  .photo-inhaler {
    left: 263px; top: 40px; width: 317px; height: 242px;
    background: linear-gradient(135deg, #c9bcae 0%, var(--photo-child) 60%, #6f7377 100%);
  }
  .photo-bandage {
    left: 0; top: 282px; width: 263px; height: 408px;
    background: linear-gradient(160deg, #c79b72 0%, var(--photo-kitchen) 45%, #e8d6c4 75%, #4a3b34 100%);
  }
  .info-panel {
    left: 263px; top: 282px; width: 586px; height: 408px;
    background: var(--orange);
    padding: 33px 20px 0 46px;
    color: var(--white);
    font-size: 16.6px;
    line-height: 26px;
    white-space: nowrap;
  }
  .info-panel p + p { margin-top: 15px; }
  .photo-play {
    left: 263px; top: 690px; width: 586px; height: 388px;
    background: linear-gradient(180deg, var(--photo-play) 0%, #e98a6f 45%, #3f6fc0 72%, #e7b6b6 100%);
  }
  .spring-offer {
    left: 40px; top: 730px; width: 200px;
    color: var(--orange);
    font-size: 16px; line-height: 22px;
  }
  .spring-offer h2 {
    font-size: 24px; line-height: 28px; font-weight: 700;
    margin-bottom: 8px;
  }
  .spring-offer .conditions { font-size: 13px; margin-top: 6px; color: var(--ink); }
  .rto { margin-top: 18px; font-size: 14px; line-height: 19px; color: var(--ink); }
  .brand {
    position: absolute;
    left: 70px; top: 1102px;
    display: flex; align-items: center; gap: 10px;
  }
  .brand-dot { width: 18px; height: 18px; border-radius: 50%; background: var(--orange-soft); flex: none; }
  .brand-name {
    font-size: 26px; line-height: 27px; font-weight: 700;
    color: var(--orange-soft);
  }
  .contact {
    position: absolute;
    left: 267px; top: 1110px;
    font-size: 15.6px; line-height: 22px;
    color: var(--ink);
  }
  .contact strong { font-weight: 700; }
</style>
</head>
<body>
<main class="flyer">
  <div class="block accent-yellow"></div>
  <div class="block photo-inhaler" role="img" aria-label="Photo of a young child using an asthma inhaler"></div>
  <div class="block photo-bandage" role="img" aria-label="Photo of a carer applying a bandage to a girl's knee beside a first aid kit"></div>

  <section class="block info-panel">
    <p>The training sessions available are the NEW childcare specific course:<br>HLTAID004 Provide an emergency first aid response in an education<br>and care setting and HLTAID003 Provide First Aid, HLTAID001<br>Provide Cardiopulmonary Resuscitation (CPR) and 22024VIC Course<br>in emergency management of asthma in the workplace And 22099VIC<br>Course in First Aid Management of Anaphylaxis.</p>
    <p>We provide a flexible, cost effective and reliable service.</p>
    <p>We have training locations available in Blackburn, Preston, Narre Warren<br>and Mornington and can also provide onsite training.</p>
    <p>We can also provide education and PRIVOS regulation consultation to<br>the childcare provider.</p>
  </section>

  <section class="block spring-offer">
    <h2>Spring Special</h2>
    <p>Receive a $50 VOLM gift card and 50% off your second training session.</p>
    <p class="conditions">*Conditions apply</p>
    <p class="rto">Registered Training Organisation<br>TOID: 47318</p>
  </section>

  <div class="block photo-play" role="img" aria-label="Photo of cheering children with arms raised in a colourful play room"></div>

  <div class="brand">
    <span class="brand-dot"></span>
    <span class="brand-name">Crestwell<br>Learning</span>
  </div>

  <footer class="contact">
    <div><strong>Phone:</strong> (03) 5127 6481 <strong>|</strong> <strong>Website:</strong> www.crestwelllearning.com.au</div>
    <div><strong>Email:</strong> marapenn@crestwelllearning.com.au</div>
  </footer>
</main>
</body>
</html>
```